6 Sizes Set - Static Banners

We have an html template for our newsletter which include graphic elements and we need images to populate these fixed Grey spaces.

Attachment 1: PLEASE READ FULL Graphic Brief is the complete brief describing all fine details.

Attachment 2: layout, shows the example of template

Attachment 3: We need the 6 image sizes (i.e. different fonts, backgrounds, colors, casino icons) – attached Styles Folder for an idea of the variety. These are just a few examples.

Target Market(s)

global

Industry/Entity Type

Casino

Requirements
Must have
• Refer to attach Full brief, for complete explanation
Nice to have
• Second Place: refer to Screenshot
Perfect example of what to submit

```html
<!DOCTYPE html>
<html lang="en">
<head>
<meta charset="utf-8">
<title>Free Games Banner Set</title>
<link href="https://fonts.googleapis.com/css2?family=Exo+2:wght@500;700&family=Russo+One&family=Lobster&family=Titillium+Web:wght@700&display=swap" rel="stylesheet">
<style>
:root{
  --page-light:#eef0f4; --page-dark:#bcc1cf;
  --teal-top:#1f6f70; --teal-bottom:#062224;
  --black-top:#2b2b2b; --black-bottom:#050505;
  --navy-top:#3d6a93; --navy-bottom:#050d18;
  --red-top:#c4141a; --red-bottom:#5d0306;
  --plum-top:#5e3a63; --plum-bottom:#1c0d20;
  --gold-light:#fff1a8; --gold:#e3b43a; --gold-dark:#8a5a10;
  --silver-light:#ffffff; --silver:#c9ced6; --silver-dark:#6d7480;
  --notch:#f2f3f6;
  --chip:#d8262c; --dice:#c0181e; --card:#e7ebef; --wheel:#3c7a22; --clover:#5aa12a; --cherry:#c8141c;
}
*{box-sizing:border-box;margin:0;padding:0}
html,body{width:1200px;height:900px;overflow:hidden}
body{background:radial-gradient(ellipse at 50% 45%,var(--page-light) 0%,#d6d9e2 60%,var(--page-dark) 100%);font-family:"Titillium Web",sans-serif;position:relative}

.banner{position:absolute;overflow:hidden;display:flex;align-items:center;justify-content:center;text-align:center;line-height:.95}
.banner::after{content:"";position:absolute;left:50%;bottom:0;transform:translateX(-50%);border:7px solid transparent;border-bottom-color:var(--notch);border-top:0}
.banner.notch-top::after{bottom:auto;top:0;border-bottom:0;border-top:7px solid var(--notch)}
.banner.no-notch::after{display:none}

.teal{background:linear-gradient(180deg,var(--teal-top),var(--teal-bottom))}
.black{background:linear-gradient(180deg,var(--black-top),var(--black-bottom))}
.navy{background:linear-gradient(180deg,var(--navy-top) 0%,#142a42 45%,var(--navy-bottom))}
.red{background:linear-gradient(160deg,var(--red-top),var(--red-bottom))}
.plum{background:linear-gradient(180deg,var(--plum-top),var(--plum-bottom))}

.title{position:relative;z-index:2;background-clip:text;-webkit-background-clip:text;color:transparent;filter:drop-shadow(0 2px 2px rgba(0,0,0,.7))}
.title.chrome{font-family:"Exo 2",sans-serif;font-weight:500;background-image:linear-gradient(180deg,var(--silver-light) 0%,var(--silver) 50%,var(--silver-dark) 52%,var(--silver-light) 100%)}
.title.marquee{font-family:"Russo One",sans-serif;letter-spacing:.04em;background-image:radial-gradient(circle,var(--gold-light) 0 35%,var(--gold) 45%,var(--gold-dark) 70%);background-size:5px 5px}
.title.script{font-family:"Lobster",cursive;background-image:linear-gradient(180deg,var(--gold-light),var(--gold) 55%,var(--gold-dark))}
.title.steel{font-family:"Russo One",sans-serif;background-image:linear-gradient(180deg,var(--silver-light),var(--silver) 48%,var(--silver-dark) 52%,#e8ebf0)}

.art{position:absolute;z-index:1;border-radius:6px}
.art.chips{background:radial-gradient(circle,#fff 0 20%,var(--chip) 22% 60%,transparent 62%)}
.art.dice{background:radial-gradient(circle at 40% 50%,var(--dice) 0 45%,transparent 60%)}
.art.suit{background:linear-gradient(180deg,#3a3a3a,#111);border:1px solid #555}
.art.cards{background:linear-gradient(180deg,var(--card),#9aa6b2)}
.art.wheel{border-radius:50%;background:radial-gradient(circle,var(--wheel) 0 45%,#1a1a1a 47% 55%,#b31218 57% 80%,#c9a24a 82%)}
.art.clover{border-radius:50%;background:radial-gradient(circle,var(--clover),#2e6a12)}
.art.cherries{background:radial-gradient(circle at 30% 65%,var(--cherry) 0 18%,transparent 20%),radial-gradient(circle at 70% 65%,var(--cherry) 0 18%,transparent 20%)}
.art.roulette{border-radius:50%;background:radial-gradient(circle,#777 0 30%,#333 45%,#999 60%,transparent 62%)}

.button{position:absolute;width:157px;height:44px;border-radius:4px;display:flex;align-items:center;justify-content:space-between;padding:0 10px 0 18px;color:#fff;font-size:17px;box-shadow:0 1px 2px rgba(0,0,0,.4)}
.button.small-label{font-size:14px;padding-left:8px}
.button svg{width:30px;height:30px;flex:none}
.btn-black{background:linear-gradient(180deg,#6a6a6a,#0c0c0c 50%,#000)}
.btn-teal{background:linear-gradient(180deg,#3d9db0,#0d5a6b)}
.btn-purple{background:linear-gradient(180deg,#5c1a72,#2b0436)}
.btn-grey{background:linear-gradient(180deg,#8a8a8a,#3c3c3c)}
.btn-red{background:linear-gradient(180deg,#a21a1a,#5c0505)}
.btn-green{background:linear-gradient(180deg,#1b7a1b,#0a420a)}
</style>
</head>
<body>

<!-- top leaderboard row 200x48 -->
<div class="banner teal notch-top" style="left:54px;top:22px;width:200px;height:48px">
  <div class="art chips" role="img" aria-label="Red casino chips" style="left:4px;top:14px;width:40px;height:34px"></div>
  <div class="art dice" role="img" aria-label="Red dice" style="right:8px;top:14px;width:34px;height:34px"></div>
  <span class="title chrome" style="font-size:24px">Free Games</span>
</div>
<div class="banner black notch-top" style="left:282px;top:22px;width:200px;height:48px">
  <span class="title marquee" style="font-size:30px;letter-spacing:0">FREE GAMES</span>
  <div class="art suit" role="img" aria-label="Spade icon tile" style="right:4px;top:6px;width:32px;height:32px"></div>
</div>
<div class="banner navy notch-top" style="left:502px;top:22px;width:200px;height:48px">
  <div class="art cards" role="img" aria-label="Playing cards" style="left:4px;top:4px;width:26px;height:36px"></div>
  <span class="title marquee" style="font-size:17px">FREE GAMES</span>
  <div class="art cards" role="img" aria-label="Playing cards" style="right:4px;top:4px;width:26px;height:36px"></div>
</div>
<div class="banner red notch-top" style="left:722px;top:22px;width:200px;height:48px">
  <div class="art wheel" role="img" aria-label="Roulette wheel" style="left:-16px;top:4px;width:40px;height:40px"></div>
  <span class="title script" style="font-size:25px">Free Games</span>
  <div class="art clover" role="img" aria-label="Clover with play icon" style="right:6px;top:12px;width:22px;height:22px"></div>
</div>
<div class="banner plum notch-top" style="left:946px;top:22px;width:200px;height:48px">
  <span class="title steel" style="font-size:24px">FREE GAMES</span>
  <div class="art dice" role="img" aria-label="Red dice" style="right:4px;top:18px;width:26px;height:26px"></div>
</div>

<!-- left column 200x130 -->
<div class="banner teal" style="left:54px;top:99px;width:200px;height:130px">
  <div class="art chips" role="img" aria-label="Red casino chips" style="left:6px;top:80px;width:80px;height:40px"></div>
  <div class="art dice" role="img" aria-label="Red dice" style="right:10px;top:78px;width:50px;height:40px"></div>
  <span class="title chrome" style="font-size:40px;margin-top:-20px">Free<br>Games</span>
</div>
<div class="banner black" style="left:54px;top:245px;width:200px;height:130px">
  <div class="art suit" role="img" aria-label="Spade icon tile" style="right:14px;top:22px;width:34px;height:34px"></div>
  <span class="title marquee" style="font-size:40px">FREE<br>GAMES</span>
</div>
<div class="banner navy" style="left:54px;top:390px;width:200px;height:130px">
  <div class="art cards" role="img" aria-label="Playing cards" style="right:8px;top:10px;width:44px;height:50px"></div>
  <span class="title marquee" style="font-size:38px;margin-top:10px">FREE<br>GAMES</span>
</div>
<div class="banner red" style="left:54px;top:532px;width:200px;height:130px">
  <div class="art wheel" role="img" aria-label="Roulette wheel" style="left:-30px;top:-20px;width:80px;height:80px"></div>
  <div class="art clover" role="img" aria-label="Clover with play icon" style="right:6px;top:82px;width:40px;height:40px"></div>
  <span class="title script" style="font-size:42px">Free<br>Games</span>
</div>
<div class="banner plum" style="left:54px;top:677px;width:200px;height:130px">
  <div class="art cherries" role="img" aria-label="Cherries" style="left:64px;top:6px;width:70px;height:24px"></div>
  <div class="art dice" role="img" aria-label="Red dice" style="left:4px;top:80px;width:40px;height:40px"></div>
  <span class="title steel" style="font-size:40px;margin-top:14px">FREE<br>GAMES</span>
</div>

<!-- wide banners 640x90 -->
<div class="banner teal" style="left:296px;top:99px;width:640px;height:90px">
  <div class="art chips" role="img" aria-label="Red casino chip with stars" style="left:24px;top:14px;width:70px;height:62px"></div>
  <div class="art dice" role="img" aria-label="Pair of red dice" style="right:24px;top:8px;width:90px;height:72px"></div>
  <span class="title chrome" style="font-size:52px">Free Games</span>
</div>
<div class="banner black" style="left:296px;top:207px;width:640px;height:90px">
  <div class="art suit" role="img" aria-label="Spade icon tile" style="left:32px;top:20px;width:52px;height:52px"></div>
  <span class="title marquee" style="font-size:62px;letter-spacing:.08em">FREE GAMES</span>
  <div class="art suit" role="img" aria-label="Heart icon tile" style="right:32px;top:20px;width:52px;height:52px"></div>
</div>
<div class="banner navy" style="left:296px;top:316px;width:640px;height:90px">
  <div class="art cards" role="img" aria-label="Playing cards" style="left:6px;top:8px;width:84px;height:76px"></div>
  <span class="title marquee" style="font-size:56px">FREE GAMES</span>
  <div class="art cards" role="img" aria-label="Playing cards" style="right:6px;top:8px;width:84px;height:76px"></div>
</div>
<div class="banner red" style="left:296px;top:426px;width:640px;height:90px">
  <div class="art wheel" role="img" aria-label="Roulette wheel with red ribbons" style="left:32px;top:-4px;width:128px;height:98px"></div>
  <span class="title script" style="font-size:52px;margin-left:60px">Free Games</span>
  <div class="art clover" role="img" aria-label="Clover with play icon" style="right:36px;top:18px;width:52px;height:52px"></div>
</div>
<div class="banner plum" style="left:296px;top:536px;width:640px;height:90px">
  <div class="art roulette" role="img" aria-label="Roulette wheel and red dice" style="left:0;top:2px;width:150px;height:88px"></div>
  <span class="title steel" style="font-size:46px;margin-right:110px;margin-left:60px">FREE GAMES</span>
  <div class="art cherries" role="img" aria-label="Cherries on slot reels" style="right:30px;top:12px;width:130px;height:64px"></div>
</div>

<!-- squares 70x80 -->
<div class="banner teal no-notch" style="left:982px;top:96px;width:70px;height:80px">
  <span class="title chrome" style="font-size:18px;transform:rotate(-30deg)">Free<br>Games</span>
</div>
<div class="banner black no-notch" style="left:982px;top:204px;width:70px;height:80px">
  <span class="title marquee" style="font-size:20px;letter-spacing:0;margin-top:-16px">FREE<br>GAMES</span>
</div>
<div class="banner navy no-notch" style="left:982px;top:311px;width:70px;height:80px">
  <span class="title marquee" style="font-size:16px;letter-spacing:0">FREE<br>GAMES</span>
</div>
<div class="banner red no-notch" style="left:982px;top:425px;width:70px;height:80px">
  <span class="title script" style="font-size:20px;transform:rotate(-30deg)">Free<br>Games</span>
</div>
<div class="banner plum no-notch" style="left:982px;top:536px;width:70px;height:80px">
  <span class="title steel" style="font-size:16px;transform:rotate(-30deg)">FREE<br>GAMES</span>
</div>

<!-- tiny 45x45 -->
<div class="banner teal no-notch" style="left:1093px;top:116px;width:45px;height:45px"><span class="title chrome" style="font-size:11px;transform:rotate(-30deg)">Free<br>Games</span></div>
<div class="banner black no-notch" style="left:1093px;top:222px;width:45px;height:45px"><span class="title marquee" style="font-size:13px;letter-spacing:0">FREE<br>GAMES</span></div>
<div class="banner navy no-notch" style="left:1093px;top:331px;width:45px;height:45px"><span class="title marquee" style="font-size:10px;letter-spacing:0">FREE<br>GAMES</span></div>
<div class="banner red no-notch" style="left:1093px;top:443px;width:45px;height:45px"><span class="title script" style="font-size:12px;transform:rotate(-30deg)">Free<br>Games</span></div>
<div class="banner plum no-notch" style="left:1093px;top:548px;width:45px;height:45px"><span class="title steel" style="font-size:10px;transform:rotate(-30deg)">FREE<br>GAMES</span></div>

<!-- call-to-action buttons -->
<a class="button btn-black" style="left:364px;top:695px">Learn more<svg viewBox="0 0 30 30"><circle cx="15" cy="15" r="14" fill="#f3f3f3"/><circle cx="15" cy="15" r="10.5" fill="#5aa322"/><path d="M12 10 L20 15 L12 20Z" fill="#fff"/></svg></a>
<a class="button btn-teal" style="left:538px;top:695px">More info<svg viewBox="0 0 30 30"><circle cx="15" cy="15" r="14" fill="#f3f3f3"/><circle cx="15" cy="15" r="10.5" fill="#9aa0a8"/><path d="M12 10 L20 15 L12 20Z" fill="#fff"/></svg></a>
<a class="button btn-purple small-label" style="left:716px;top:695px">Register for Free<svg viewBox="0 0 30 30"><circle cx="15" cy="15" r="14" fill="#f3f3f3"/><circle cx="15" cy="15" r="10.5" fill="#f0a114"/><path d="M12 10 L20 15 L12 20Z" fill="#fff"/></svg></a>
<a class="button btn-grey small-label" style="left:895px;top:695px;font-size:15px;padding-left:12px">Join Here Now<svg viewBox="0 0 30 30"><circle cx="15" cy="15" r="14" fill="#f3f3f3"/><circle cx="15" cy="15" r="10.5" fill="#2c8fe0"/><path d="M12 10 L20 15 L12 20Z" fill="#fff"/></svg></a>
<a class="button btn-red" style="left:449px;top:759px">Click Here<svg viewBox="0 0 30 30"><circle cx="15" cy="15" r="14" fill="#f3f3f3"/><circle cx="15" cy="15" r="10.5" fill="#f0a114"/><path d="M12 10 L20 15 L12 20Z" fill="#fff"/></svg></a>
<a class="button btn-teal" style="left:626px;top:759px">Play Now<svg viewBox="0 0 30 30"><circle cx="15" cy="15" r="14" fill="#f3f3f3"/><circle cx="15" cy="15" r="10.5" fill="#9aa0a8"/><path d="M12 10 L20 15 L12 20Z" fill="#fff"/></svg></a>
<a class="button btn-green" style="left:804px;top:759px">Join Free<svg viewBox="0 0 30 30"><circle cx="15" cy="15" r="14" fill="#f3f3f3"/><circle cx="15" cy="15" r="10.5" fill="#9aa0a8"/><path d="M12 10 L20 15 L12 20Z" fill="#fff"/></svg></a>

</body>
</html>
```